Property letting UK website

I need a web design for a new Property letting company in the UK. I already have a logo that was produced and won by a brief forge logo designer last week.

I like modern designs and require ease of functionality and usage. I already have a domain name registered so need to be able to link to that domain.

Regards,

Morven.

Target Market(s)

UK property

Industry/Entity Type

It Company

Number of Pages Required

5+ page

Requirements
Must have
• Home page, Current properties to let page, About us page, Contact us page, Testimonials page and ability to link to twitter and Facebook account.

```html
<!DOCTYPE html>
<html lang="en">
<head>
<meta charset="utf-8">
<title>Homeward Lets – Property Rent &amp; Lease</title>
<link href="https://fonts.googleapis.com/css2?family=Mulish:ital,wght@0,300;0,400;0,600;1,400&family=Libre+Baskerville&display=swap" rel="stylesheet">
<style>
:root{
  --header-bg:#140b0b;
  --logo-bg:#050303;
  --blue:#0ea5e6;
  --blue-text:#1aa4de;
  --intro-bg:#f4f4f4;
  --text-dark:#1d1d1d;
  --text-mid:#555;
  --text-light:#7a7a7a;
  --white:#fff;
  --footer-bg:#2b2b2b;
}
*{margin:0;padding:0;box-sizing:border-box}
html,body{width:794px;height:1200px;overflow:hidden}
body{position:relative;font-family:"Mulish",sans-serif;background:var(--white);color:var(--text-dark)}
.abs{position:absolute}

.site-header{left:0;top:0;width:794px;height:77px;background:var(--header-bg)}
.logo{left:80px;top:0;width:168px;height:77px;background:var(--logo-bg);display:flex;align-items:center;justify-content:center;gap:7px;color:var(--white);font-size:17px;font-weight:400}
.logo .mark{width:10px;height:10px;background:var(--blue)}
.phone{right:108px;top:14px;display:flex;align-items:center;gap:4px;color:var(--blue-text);font-size:13px}
.main-nav{top:44px;right:108px;display:flex;gap:22px;font-size:11.5px;color:var(--white)}

.hero{left:0;top:77px;width:794px;height:336px;background:linear-gradient(180deg,#6e88a8 0%,#7b6a58 30%,#8a7562 55%,#5f8a3e 78%,#3f6f2a 100%)}
.hero-caption{left:174px;top:201px;width:410px;height:78px;background:rgba(20,16,14,.72);text-align:center;color:var(--white);font-family:"Libre Baskerville",serif;border-bottom:2px solid rgba(255,255,255,.35)}
.hero-caption h1{font-weight:400;font-size:27px;margin-top:14px;letter-spacing:.5px}
.hero-caption p{font-size:15px;margin-top:2px}
.slider-dots{left:378px;top:396px;display:flex;gap:3px}
.slider-dots span{width:8px;height:8px;border-radius:50%;background:var(--white)}

.intro{left:0;top:413px;width:794px;height:172px;background:var(--intro-bg);text-align:center}
.intro h2{font-weight:400;font-size:21px;margin-top:28px}
.intro h3{font-weight:400;font-size:14px;color:#333;margin-top:2px}
.intro p{font-size:8px;color:var(--text-light);line-height:13px;margin:0 auto;width:600px}
.intro .p1{margin-top:10px}
.intro .p2{margin-top:4px}
.btn{display:inline-block;margin-top:10px;background:var(--blue);color:var(--white);font-size:8px;font-weight:600;padding:6px 12px;border-radius:2px}
.notch{left:0;top:584px}

.properties-title{left:0;top:618px;width:794px;text-align:center;font-size:20px;font-weight:300}
.card{top:664px;width:142px;height:149px;background:var(--white);box-shadow:0 4px 6px rgba(0,0,0,.12);border:1px solid #e6e6e6}
.card .photo{height:86px}
.card h4{font-weight:400;color:var(--blue-text);font-size:12px;margin:8px 0 0 13px}
.card p{font-size:7px;color:var(--text-light);line-height:12.5px;margin:3px 10px 0 13px}

.testimonials{left:0;top:879px;width:794px;height:242px;background:var(--blue);color:var(--white);text-align:center}
.testimonials h2{font-weight:300;font-size:19px;margin-top:27px}
.quote{top:941px;width:190px;text-align:center}
.avatar{width:60px;height:60px;border-radius:50%;border:3px solid var(--white);margin:0 auto;background:linear-gradient(160deg,#d9b89a,#8b6a55)}
.quote blockquote{font-style:italic;font-size:8px;line-height:12.2px;margin-top:17px;position:relative;padding:0 6px}
.quote blockquote::before{content:"\201C";position:absolute;left:-8px;top:-6px;font-size:22px;font-style:normal}
.quote blockquote::after{content:"\201D";position:absolute;right:-8px;bottom:-14px;font-size:22px;font-style:normal}
.quote cite{display:block;font-style:normal;font-size:8.5px;margin-top:5px}

.site-footer{left:0;top:1121px;width:794px;height:79px;background:var(--footer-bg);color:var(--white)}
.footer-nav{left:102px;top:25px;font-size:10px;display:flex;gap:5px}
.copyright{left:102px;top:44px;font-size:7px;color:#bbb}
.social{top:24px;width:15px;height:15px;border-radius:2px}
</style>
</head>
<body>

<header class="site-header abs">
  <div class="logo abs"><span class="mark"></span>Homeward Lets</div>
  <div class="phone abs">
    <svg width="16" height="16" viewBox="0 0 16 16"><circle cx="8" cy="8" r="7" fill="none" stroke="#fff" stroke-width="1.2"/><path d="M5.6 4.4l1.2 1.6-.7 1c.5 1 1.3 1.8 2.3 2.3l1-.7 1.6 1.2-.7 1.3c-2.8-.4-5-2.6-5.4-5.4z" fill="#fff"/></svg>
    555.204.7731
  </div>
  <nav class="main-nav abs">
    <span>Home</span><span>Current Properties</span><span>About us</span><span>Testimonials</span><span>Contact us</span>
  </nav>
</header>

<section class="hero abs" role="img" aria-label="Family sitting on a lawn in front of a stone suburban house"></section>
<div class="hero-caption abs">
  <h1>PROPERTY RENT &amp; LEASE</h1>
  <p>MORBI PORTA LIBERO ULLAMCORPER</p>
</div>
<div class="slider-dots abs"><span></span><span></span><span></span><span></span></div>

<section class="intro abs">
  <h2>Vivamus porttitor purus nisi eleifend libero tempus</h2>
  <h3>Bibendum accumsan vestibulum ut commodo Morbi</h3>
  <p class="p1">Phasellus pellentesque aliquam enim Proin dui lectus cursus eu mattis laoreet viverra sit amet quam Curabitur vel dolor ultrices ipsum</p>
  <p class="p2">Curabitur vel mi sit amet magna malesuada ultrices Ut nisi erat fermentum vel congue id euismod in elit Fusce ultricies orci ac feugiat suscipit leo massa sodales velit et scelerisque mi tortor at ipsum Proin orci odio commodo ac gravida non tristique vel tellus Pellentesque nibh</p>
  <span class="btn">READ MORE</span>
</section>
<svg class="notch abs" width="794" height="30" viewBox="0 0 794 30">
  <path d="M0 1H376C388 1 392 10 397 28C402 10 406 1 418 1H794V0H0Z" fill="#f4f4f4"/>
  <path d="M376 1C388 1 392 10 397 28C402 10 406 1 418 1" fill="none" stroke="#e4e4e4"/>
</svg>

<h2 class="properties-title abs">Current Properties</h2>
<article class="card abs" style="left:102px">
  <div class="photo" role="img" aria-label="Green cottage with white picket fence" style="background:linear-gradient(180deg,#7fa6cf,#9fb08a 55%,#4d8a3a)"></div>
  <h4>Property Tittle</h4>
  <p>Etiam est nunc venenatis in tris­tiquimperdiet ac nisl Cum</p>
</article>
<article class="card abs" style="left:253px">
  <div class="photo" role="img" aria-label="Grey house with garden flowers" style="background:linear-gradient(180deg,#6f7d6a,#a5a49a 50%,#3f6b2e)"></div>
  <h4>Property Tittle</h4>
  <p>Etiam est nunc venenatis in tris­tiquimperdiet ac nisl Cum</p>
</article>
<article class="card abs" style="left:404px">
  <div class="photo" role="img" aria-label="Beige house among autumn trees" style="background:linear-gradient(180deg,#b5622a,#d8b592 55%,#6a5a3a)"></div>
  <h4>Property Tittle</h4>
  <p>Etiam est nunc venenatis in tris­tiquimperdiet ac nisl Cum</p>
</article>
<article class="card abs" style="left:555px">
  <div class="photo" role="img" aria-label="Mediterranean style villa with palm trees" style="background:linear-gradient(180deg,#86b0d8,#c9ac86 55%,#5d7a3e)"></div>
  <h4>Property Tittle</h4>
  <p>Etiam est nunc venenatis in tris­tiquimperdiet ac nisl Cum</p>
</article>

<section class="testimonials abs">
  <svg class="abs" style="left:386px;top:0" width="20" height="10" viewBox="0 0 20 10"><path d="M0 0H20L10 10Z" fill="#fff"/></svg>
  <h2>Customer Testimonials</h2>
</section>
<div class="quote abs" style="left:108px">
  <div class="avatar" role="img" aria-label="Customer portrait"></div>
  <blockquote>Mauris vel lacus vitae felis vestibulum volut­pat Etiam est nunc venenatis in tristique eu imperdiet ac nisl Cum sociis natoque penati­bus et magnis dis parturient montes</blockquote>
  <cite>By Author Name</cite>
</div>
<div class="quote abs" style="left:313px">
  <div class="avatar" role="img" aria-label="Customer portrait"></div>
  <blockquote>Mauris vel lacus vitae felis vestibulum volut­pat Etiam est nunc venenatis in tristique eu imperdiet ac nisl Cum sociis natoque penati­bus et magnis dis parturient montes</blockquote>
  <cite>By Author Name</cite>
</div>
<div class="quote abs" style="left:511px">
  <div class="avatar" role="img" aria-label="Customer portrait"></div>
  <blockquote>Mauris vel lacus vitae felis vestibulum volut­pat Etiam est nunc venenatis in tristique eu imperdiet ac nisl Cum sociis natoque penati­bus et magnis dis parturient montes</blockquote>
  <cite>By Author Name</cite>
</div>

<footer class="site-footer abs">
  <nav class="footer-nav abs">
    <span>Home</span><span>|</span><span>Current Properties</span><span>|</span><span>About us</span><span>|</span><span>Testimonials</span><span>|</span><span>Contact us</span>
  </nav>
  <p class="copyright abs">© 2014 Company Name &nbsp;All right reserved &nbsp;Term of Use</p>
  <span class="social abs" style="left:660px;background:#3b5a9a"></span>
  <span class="social abs" style="left:680px;background:#34a8de"></span>
</footer>

</body>
</html>
```